VORTA Diagnostics Pooling One Sheet

The process and concept for pooling is to target large populations of people; i.e. a school, prison, employer (where people are isolated by pods), then to test them all in one controllable group. By breaking down the pool size (ideally is 12 or 16 max) then when a positive pool pops up, the entity has the lab automatically reflex to test the whole pool to determine who is positive. During that exchange, several workflows could take place from the population that was being tested. This type of pooled testing is called Surveillance testing ,when it reflects, then it goes to Screening or Diagnostic testing.

The workflow is:
School/employer collects all patient information captured on a requisition form or electronically (w signature) and DOES NOT send to VORTA
School/employer collects individual specimens and labels them with a unique bar code (non-repeating and can include the DOB)
School/employer is responsible for housing and managing all the unique patient information for each individual specimen
School/employer delivers specimens to VORTA and School/employer directs VORTA what specimens are in what designated pool (one pool size for entire project)
When a pool is positive, VORTA notifies School/employer
When reflex testing in indicated for client, School/employer submits to VORTA on demand all patient information needed to process the reflexed option
VORTA reports back to School/employer in 12 hours the results of the retest
https://www.healthbureau-example.test/medical-devices/coronavirus-covid-19-and-medical-devices/pooled-sample-testing-and-screening-testing-covid-19
https://www.mediquestlabs.test/coronavirus-disease-covid-19/news/mediquest-receives-authorization-covid-19-sample-pooling

Target Market(s)

Schools, Universities, Employers

Font styles to use
Sans Serif

Colors
85acd3
85cae6
34a6d7

Requirements
Must have
• VORTA branded along with an elegant yet clinical feel. have all contact information for VORTA Diagnostics. Go to www.vortadx.test for all info

```html
<!DOCTYPE html>
<html lang="en">
<head>
<meta charset="utf-8">
<title>VORTA Diagnostics – Pooling One Sheet</title>
<link rel="stylesheet" href="https://fonts.googleapis.com/css2?family=Lato:wght@400;700;900&display=swap">
<style>
  :root {
    --page-bg: #e9f3f9;
    --sheet: #ffffff;
    --navy: #2b3d4c;
    --blue: #1d8fd8;
    --blue-light: #34a6d7;
    --sky: #85cae6;
    --steel: #85acd3;
    --deep: #183a78;
    --tick: #2a9ad6;
    --ink: #1f2328;
  }
  * { margin: 0; padding: 0; box-sizing: border-box; }
  html, body { width: 1200px; height: 1200px; overflow: hidden; background: var(--page-bg); }
  body { font-family: "Lato", Arial, sans-serif; color: var(--ink); }

  .sheet {
    position: absolute; left: 223px; top: 72px;
    width: 753px; height: 1056px;
    background: var(--sheet); overflow: hidden;
  }
  .brand {
    position: absolute; left: 58px; top: 58px;
    display: flex; align-items: center; gap: 12px;
  }
  .brand-mark { width: 34px; height: 34px; background: var(--blue-light); }
  .brand-name { font-weight: 900; font-size: 36px; color: var(--navy); letter-spacing: 0.5px; }

  .intro-band {
    position: absolute; left: 0; top: 141px; width: 753px; height: 301px;
    background: linear-gradient(100deg, var(--blue) 0%, var(--blue-light) 70%, var(--blue) 100%);
  }
  .intro-text {
    position: absolute; left: 55px; top: 162px; width: 290px;
    color: #fff; font-size: 14.3px; line-height: 17.8px;
  }
  .hex-art { position: absolute; left: 0; top: 0; }

  .workflow-title {
    position: absolute; left: 55px; top: 483px;
    width: 237px; height: 41px; padding-left: 17px;
    background: var(--navy); color: #fff;
    border-radius: 0 21px 21px 0;
    font-weight: 900; font-size: 21px; line-height: 41px; letter-spacing: -0.3px;
  }
  .workflow-list {
    position: absolute; left: 55px; top: 555px; width: 640px;
    list-style: none;
  }
  .workflow-list li {
    position: relative; padding-left: 29px; margin-bottom: 12.5px;
    font-size: 14.3px; line-height: 17.9px;
  }
  .workflow-list svg { position: absolute; left: 0; top: 3px; }

  .contact-band {
    position: absolute; left: 0; top: 896px; width: 753px; height: 93px;
    background: linear-gradient(90deg, var(--blue) 0%, var(--blue-light) 100%);
    color: #fff; font-weight: 900; font-size: 15px;
  }
  .contact-item { position: absolute; display: flex; align-items: flex-start; gap: 8px; line-height: 18px; }
  .contact-item svg { flex: none; margin-top: 1px; }
  .hours-band {
    position: absolute; left: 0; top: 989px; width: 753px; height: 67px;
    background: linear-gradient(90deg, var(--deep) 0%, #1f5aa6 55%, var(--deep) 100%);
    color: #fff; font-weight: 900; font-size: 17px; letter-spacing: 5.4px;
    text-align: center; line-height: 67px;
  }
</style>
</head>
<body>
<main class="sheet">
  <div class="brand">
    <span class="brand-mark"></span>
    <span class="brand-name">VORTA Diagnostics</span>
  </div>

  <section class="intro-band"></section>
  <p class="intro-text">The process and concept for pooling is to target large populations of people; i.e. a school, prison, employer (where people are isolated by pods), then to test them all in one controllable group. By breaking down the pool size (ideally is 12 or 16 max) then when a positive pool pops up, the entity has the lab automatically reflex to test the whole pool to determine who is positive. During that exchange, several workflows could take place from the population that was being tested. This type of pooled testing is called Surveillance testing, when it reflects, then it goes to Screening or Diagnostic testing.</p>

  <svg class="hex-art" width="753" height="500" viewBox="0 0 753 500">
    <defs>
      <linearGradient id="photoTone" x1="0" y1="0" x2="1" y2="1">
        <stop offset="0" stop-color="#e4eef4"/>
        <stop offset="0.55" stop-color="#c9def0"/>
        <stop offset="1" stop-color="#7fb3df"/>
      </linearGradient>
    </defs>
    <polygon points="584,30 788,147 788,395 584,500 376,395 376,147" fill="#ffffff"/>
    <polygon role="img" aria-label="Photo: health worker in protective suit and face shield taking a throat swab from a patient"
      points="584,43 777,153 777,389 584,486 391,389 391,153" fill="url(#photoTone)"/>
  </svg>

  <h2 class="workflow-title">THE WORKFLOW IS</h2>
  <ul class="workflow-list">
    <li><svg width="18" height="18" viewBox="0 0 18 18"><circle cx="9" cy="9" r="7.6" fill="none" stroke="var(--tick)" stroke-width="1.6"/><path d="M5.5 9.2l2.4 2.3 4.4-4.6" fill="none" stroke="var(--tick)" stroke-width="1.7" stroke-linecap="round" stroke-linejoin="round"/></svg>School/employer collects all patient information captured on a requisition form or electronically (w signature) and DOES NOT send to VORTA</li>
    <li><svg width="18" height="18" viewBox="0 0 18 18"><circle cx="9" cy="9" r="7.6" fill="none" stroke="var(--tick)" stroke-width="1.6"/><path d="M5.5 9.2l2.4 2.3 4.4-4.6" fill="none" stroke="var(--tick)" stroke-width="1.7" stroke-linecap="round" stroke-linejoin="round"/></svg>School/employer collects individual specimens and labels them with a unique bar code (non-repeating and can include the DOB)</li>
    <li><svg width="18" height="18" viewBox="0 0 18 18"><circle cx="9" cy="9" r="7.6" fill="none" stroke="var(--tick)" stroke-width="1.6"/><path d="M5.5 9.2l2.4 2.3 4.4-4.6" fill="none" stroke="var(--tick)" stroke-width="1.7" stroke-linecap="round" stroke-linejoin="round"/></svg>School/employer is responsible for housing and managing all the unique patient information for each individual specimen</li>
    <li><svg width="18" height="18" viewBox="0 0 18 18"><circle cx="9" cy="9" r="7.6" fill="none" stroke="var(--tick)" stroke-width="1.6"/><path d="M5.5 9.2l2.4 2.3 4.4-4.6" fill="none" stroke="var(--tick)" stroke-width="1.7" stroke-linecap="round" stroke-linejoin="round"/></svg>School/employer delivers specimens to VORTA and School/employer directs VORTA what specimens are in what designated pool (one pool size for entire project)</li>
    <li><svg width="18" height="18" viewBox="0 0 18 18"><circle cx="9" cy="9" r="7.6" fill="none" stroke="var(--tick)" stroke-width="1.6"/><path d="M5.5 9.2l2.4 2.3 4.4-4.6" fill="none" stroke="var(--tick)" stroke-width="1.7" stroke-linecap="round" stroke-linejoin="round"/></svg>When a pool is positive, VORTA notifies School/employer</li>
    <li><svg width="18" height="18" viewBox="0 0 18 18"><circle cx="9" cy="9" r="7.6" fill="none" stroke="var(--tick)" stroke-width="1.6"/><path d="M5.5 9.2l2.4 2.3 4.4-4.6" fill="none" stroke="var(--tick)" stroke-width="1.7" stroke-linecap="round" stroke-linejoin="round"/></svg>When reflex testing in indicated for client, School/employer submits to VORTA on demand all patient information needed to process the reflexed option</li>
    <li><svg width="18" height="18" viewBox="0 0 18 18"><circle cx="9" cy="9" r="7.6" fill="none" stroke="var(--tick)" stroke-width="1.6"/><path d="M5.5 9.2l2.4 2.3 4.4-4.6" fill="none" stroke="var(--tick)" stroke-width="1.7" stroke-linecap="round" stroke-linejoin="round"/></svg>VORTA reports back to School/employer in 12 hours the results of the retest</li>
  </ul>

  <footer>
    <div class="contact-band">
      <div class="contact-item" style="left:58px; top:24px;">
        <svg width="18" height="18" viewBox="0 0 24 24"><path d="M6.6 2.8l3 3.5-1.8 2.4c1.3 2.8 3.6 5.1 6.5 6.5l2.4-1.8 3.5 3-1.6 3.3C12 19.6 4.4 12 3.3 4.4z" fill="none" stroke="#fff" stroke-width="2" stroke-linejoin="round"/></svg>
        <span>800-555-0142</span>
      </div>
      <div class="contact-item" style="left:58px; top:53px;">
        <svg width="18" height="18" viewBox="0 0 24 24"><path d="M6.6 2.8l3 3.5-1.8 2.4c1.3 2.8 3.6 5.1 6.5 6.5l2.4-1.8 3.5 3-1.6 3.3C12 19.6 4.4 12 3.3 4.4z" fill="none" stroke="#fff" stroke-width="2" stroke-linejoin="round"/></svg>
        <span>240-555-0199</span>
      </div>
      <div class="contact-item" style="left:278px; top:26px;">
        <svg width="16" height="20" viewBox="0 0 16 20"><path d="M8 1a6 6 0 0 0-6 6c0 4.5 6 11 6 11s6-6.5 6-11a6 6 0 0 0-6-6z" fill="none" stroke="#fff" stroke-width="2"/><circle cx="8" cy="7" r="2.2" fill="#fff"/></svg>
        <span>1200 Meridian Way Suite B<br>Riverton, MD 21000</span>
      </div>
      <div class="contact-item" style="left:540px; top:26px;">
        <svg width="18" height="16" viewBox="0 0 20 16"><rect x="1" y="1.5" width="18" height="13" fill="none" stroke="#fff" stroke-width="2"/><path d="M1.5 2l8.5 7 8.5-7" fill="none" stroke="#fff" stroke-width="2"/></svg>
        <span>info@vortadx.test</span>
      </div>
      <div class="contact-item" style="left:540px; top:52px;">
        <svg width="18" height="18" viewBox="0 0 20 20"><circle cx="10" cy="10" r="8" fill="none" stroke="#fff" stroke-width="2"/><path d="M2 10h16M10 2c3 3 3 13 0 16M10 2c-3 3-3 13 0 16" fill="none" stroke="#fff" stroke-width="1.6"/></svg>
        <span>www.vortadx.test</span>
      </div>
    </div>
    <div class="hours-band">Hours: Monday - Friday 8am to 5pm</div>
  </footer>
</main>
</body>
</html>
```